Small and passionate motorcycle workshop requires a business card that kicks butt!

I'm Darren, I'm passionate about my motorcycles, I'm passionate about my desert racing and I'm a passionate motorcycle technician, that's why I started my own motorcycle workshop: 'Rivo Tanza'.
I started my workshop in my dining room and it’s eventually moved into a newly renovated shed that my Grandpa built with his own two hands in the early 1960's. To the customer the shed looks like a farm shed on my property, however the inside is ready for open heart surgery on their "Baby" which could be a late model sports bike, a highway cruiser, an old four-wheeler or an off road desert racing weapon!
This business is my own, I've built it from my dining room floor and I'm deeply passionate about it.
I need a professional business card and logo which looks like a heart and soul is intermingled through it because that is how my business is run. Rivo Tanza may have started from my dining room but it has always been professionally run and I have always put my passion into the bikes I've worked on.

-The text only logo needs to be comprised of 'Rivo Tanza'
-The business card will be double sided

And I do realise it will be a hard task to make something look professional and personal at the same time...however there are some very talented people in this world and I can’t wait to see what you create!

I've added some logo/designs that I'm fond of.

Industry/Entity Type

Racing

Requirements
Must have
• My name - Darren Pulkett
My Qualification - Qualified Motorcycle Technician
Ph - 0471 582 930
Email - rivotanza@quillmail.example
Address - 17 Bellbrook Lane, Kelvale, SA
ABN - 61 804 392 117 (plesase include the 'ABN' part
Needs to include these dot points:
-Servicing
-Repairs
-All makes/models
-Weekends by appt.
-Pick-up/delivery available
Nice to have
• I like the idea of calling myself a "Qualified and Passionate Motorcycle Technician". If the card does not come across that it’s a passionate business I'd like this line to be used on the card near my name.

One idea I like would include having the text only logo on the front being quite bold and contrasted to the background, then having my name and number smaller underneath somewhere. I'm very open to whatever comes my way so I'm look forward to seeing some sweet ideas!

```html
<!DOCTYPE html>
<html lang="en">
<head>
<meta charset="utf-8">
<title>Rivo Tanza Business Card</title>
<link href="https://fonts.googleapis.com/css2?family=Oxygen:wght@400;700&display=swap" rel="stylesheet">
<style>
  :root {
    --page-bg: #d9d9d9;
    --card-dark: #1c1c1c;
    --plate: #2b2b2b;
    --plate-edge: #1e1e1e;
    --metal-light: #e6e6e6;
    --metal-mid: #b9b9b9;
    --metal-dark: #8f8f8f;
    --ink: #1a1a1a;
    --ink-soft: #2e2e2e;
    --logo-ink: #f2f2f2;
    --bullet: #555555;
  }
  * { margin: 0; padding: 0; box-sizing: border-box; }
  html, body { width: 1200px; height: 861px; overflow: hidden; }
  body {
    background: var(--page-bg);
    font-family: "Oxygen", Arial, sans-serif;
    position: relative;
  }
  .card {
    position: absolute;
    top: 280px;
    width: 500px;
    height: 300px;
    background: var(--card-dark);
    overflow: hidden;
    box-shadow: 0 6px 18px rgba(0,0,0,0.35);
  }
  .card--front { left: 60px; }
  .card--back { left: 640px; }

  .card__plate {
    position: absolute;
    left: 0; right: 0;
    background: var(--plate);
  }
  .card__plate--top { top: 0; height: 140px; }
  .card__plate--bottom { top: 260px; bottom: 0; background: var(--plate-edge); }

  .card__logo {
    position: absolute;
    top: 42px; left: 0; right: 0;
    text-align: center;
    font-weight: 700;
    font-size: 52px;
    letter-spacing: 1px;
    color: var(--logo-ink);
    line-height: 1;
  }

  .card__band {
    position: absolute;
    top: 140px; left: 0; right: 0;
    height: 120px;
    background: linear-gradient(90deg, var(--metal-dark) 0%, var(--metal-light) 35%, var(--metal-mid) 60%, var(--metal-light) 85%, var(--metal-dark) 100%);
    border-top: 2px solid #5a5a5a;
    border-bottom: 2px solid #3a3a3a;
  }

  .services {
    position: absolute;
    top: 12px; left: 170px;
    list-style: none;
  }
  .services__item {
    font-size: 15px;
    font-weight: 700;
    line-height: 19.5px;
    color: var(--ink);
    display: flex;
    align-items: center;
    gap: 6px;
  }
  .services__dot {
    width: 9px; height: 9px;
    border-radius: 50%;
    background: var(--bullet);
    flex: none;
  }

  .owner {
    position: absolute;
    top: 28px; left: 46px;
  }
  .owner__name {
    font-size: 26px;
    font-weight: 700;
    color: var(--ink);
    line-height: 1.1;
  }
  .owner__title {
    margin-top: 10px;
    font-size: 12.5px;
    line-height: 17px;
    color: var(--ink-soft);
  }

  .contact {
    position: absolute;
    top: 12px; left: 290px;
    font-size: 11px;
    line-height: 15px;
    color: var(--ink);
  }
  .contact__row { margin-bottom: 5px; }
  .contact__label { font-weight: 700; }
</style>
</head>
<body>

  <section class="card card--front" aria-label="Card front">
    <div class="card__plate card__plate--top" role="img" aria-label="Dark diamond tread plate texture"></div>
    <div class="card__logo">Rivo Tanza</div>
    <div class="card__band">
      <ul class="services">
        <li class="services__item"><span class="services__dot"></span>Servicing</li>
        <li class="services__item"><span class="services__dot"></span>Repairs</li>
        <li class="services__item"><span class="services__dot"></span>All makes/models</li>
        <li class="services__item"><span class="services__dot"></span>Weekends by appointment</li>
        <li class="services__item"><span class="services__dot"></span>Pick-up/delivery available</li>
      </ul>
    </div>
    <div class="card__plate card__plate--bottom" role="img" aria-label="Dark diamond tread plate strip"></div>
  </section>

  <section class="card card--back" aria-label="Card back">
    <div class="card__plate card__plate--top" role="img" aria-label="Dark diamond tread plate texture"></div>
    <div class="card__logo">Rivo Tanza</div>
    <div class="card__band">
      <div class="owner">
        <div class="owner__name">Darren Pulkett</div>
        <div class="owner__title">Qualified and Passionate<br>Motorcycle Technician</div>
      </div>
      <div class="contact">
        <div class="contact__row"><span class="contact__label">Phone:</span> 0471 582 930</div>
        <div class="contact__row"><span class="contact__label">E-mail:</span> rivotanza@quillmail.example</div>
        <div class="contact__row"><span class="contact__label">Address:</span> 17 Bellbrook Lane,<br>Kelvale, SA</div>
        <div class="contact__row"><span class="contact__label">ABN:</span> 61 804 392 117</div>
      </div>
    </div>
    <div class="card__plate card__plate--bottom" role="img" aria-label="Dark diamond tread plate strip"></div>
  </section>

</body>
</html>
```